Business card design for Automotive workshop

We need a business card for a new automotive repair and tyre shop called Ridgeback Prime Automotive located in New Zealand. We are a clean, modern and fresh workshop and company.

Front needs to feature logo,
my name:
Lachie Westergaard (director)

Address:
48 Marlow Lane
Whitianga 3510

Phone: 07 842 1937
Mobile: 027 519 2764
Email: office@ridgebackmotors.co.nz
Website: ridgebackmotors.co.nz

Back needs to feature an area to write down appointment details, date and time.

Also feature a list of jobs and work we do such as,
Vehicle Servicing
All Mechanical Repairs
Warrant of Fitness
Tyres & Wheel Alignments
Automotive Diagnostics
Automotive Parts & Supplies

```html
<!DOCTYPE html>
<html lang="en">
<head>
<meta charset="utf-8">
<title>Ridgeback Prime Automotive – Business Card</title>
<link href="https://fonts.googleapis.com/css2?family=Montserrat:wght@500;600;700;800&family=Roboto:wght@400;500&display=swap" rel="stylesheet">
<style>
  :root {
    --red: #e31e26;
    --ink: #231f20;
    --black: #0b0b0c;
    --white: #ffffff;
    --grey: #3a3a3a;
    --rule: #8a8a8a;
    --stage: #d9d9d9;
  }
  * { box-sizing: border-box; margin: 0; padding: 0; }
  html, body { width: 1200px; height: 900px; overflow: hidden; }
  body {
    background: var(--stage);
    display: flex; flex-direction: column; align-items: center; justify-content: center;
    gap: 26px;
    font-family: "Roboto", Arial, sans-serif;
  }
  .card {
    position: relative;
    width: 680px; height: 415px;
    overflow: hidden;
    box-shadow: 0 6px 18px rgba(0,0,0,.25);
  }

  /* Shared brand line */
  .brand { position: absolute; left: 0; right: 0; display: flex; justify-content: center; }
  .brand__name {
    font-family: "Montserrat", Arial, sans-serif;
    font-weight: 800; color: var(--red);
    font-size: 30px; letter-spacing: .5px; text-transform: uppercase;
    white-space: nowrap;
    display: flex; align-items: center; gap: 12px;
  }
  .brand__mark { width: 14px; height: 14px; background: var(--red); flex: none; }

  /* Back */
  .card--back { background: var(--black); color: var(--white); }
  .card--back .brand { top: 44px; }
  .services {
    position: absolute; top: 104px; left: 0; right: 0;
    font-family: "Montserrat", Arial, sans-serif; font-weight: 500;
    font-size: 14px; line-height: 28px; text-align: center;
    list-style: none;
  }
  .services li { display: inline; }
  .services li.row-start::before { display: none; }
  .services li::before {
    content: ""; display: inline-block; width: 8px; height: 8px; border-radius: 50%;
    background: var(--red); margin: 0 10px 2px; vertical-align: middle;
  }
  .appointment {
    position: absolute; left: 60px; right: 60px; top: 200px;
    border: 1px solid var(--rule); padding: 18px 24px 20px;
    font-family: "Montserrat", Arial, sans-serif;
  }
  .appointment__title {
    font-weight: 700; font-size: 15px; text-transform: uppercase; letter-spacing: 1px;
    color: var(--red); margin-bottom: 18px;
  }
  .appointment__row { display: flex; gap: 28px; margin-top: 16px; }
  .appointment__field { flex: 1; display: flex; align-items: flex-end; gap: 10px; font-size: 14px; font-weight: 600; }
  .appointment__field span { flex: 1; border-bottom: 1px solid var(--rule); height: 18px; }
  .card--back .stripe { position: absolute; left: 0; right: 0; bottom: 0; height: 8px; background: var(--red); }

  /* Front */
  .card--front { background: var(--white); color: var(--ink); }
  .card--front .brand { top: 58px; }
  .person {
    position: absolute; top: 178px; right: 352px; text-align: right;
    font-family: "Montserrat", Arial, sans-serif;
  }
  .person__name { color: var(--red); font-weight: 700; font-size: 22px; text-transform: uppercase; letter-spacing: -.3px; white-space: nowrap; }
  .person__role { color: var(--grey); font-weight: 700; font-size: 19px; margin-top: 4px; }
  .divider { position: absolute; left: 345px; top: 170px; width: 2px; height: 96px; background: var(--ink); }
  .contacts { position: absolute; left: 368px; top: 168px; list-style: none; font-size: 16px; color: var(--grey); }
  .contacts li { display: flex; align-items: center; gap: 8px; height: 25px; white-space: nowrap; }
  .contacts svg { width: 15px; height: 15px; flex: none; fill: var(--red); }
  .address {
    position: absolute; left: 0; right: 0; top: 308px;
    display: flex; justify-content: center; align-items: center; gap: 8px;
    font-size: 17px; color: var(--grey); font-weight: 500;
  }
  .address svg { width: 14px; height: 18px; fill: var(--red); }
  .card--front .stripe { position: absolute; left: 0; bottom: 0; width: 680px; height: 14px; }
</style>
</head>
<body>

<section class="card card--back" aria-label="Card back">
  <div class="brand">
    <span class="brand__name"><span class="brand__mark"></span>Ridgeback Prime Automotive</span>
  </div>
  <ul class="services">
    <li class="row-start">Vehicle Servicing</li><li>All Mechanical Repairs</li><li>Warrant of Fitness</li><br>
    <li class="row-start">Tyres &amp; Wheel Alignments</li><li>Automotive Diagnostics</li><li>Automotive Parts &amp; Supplies</li>
  </ul>
  <div class="appointment">
    <p class="appointment__title">Your Next Appointment</p>
    <div class="appointment__row">
      <p class="appointment__field">Details<span></span></p>
    </div>
    <div class="appointment__row">
      <p class="appointment__field">Date<span></span></p>
      <p class="appointment__field">Time<span></span></p>
    </div>
  </div>
  <div class="stripe"></div>
</section>

<section class="card card--front" aria-label="Card front">
  <div class="brand">
    <span class="brand__name"><span class="brand__mark"></span>Ridgeback Prime Automotive</span>
  </div>

  <div class="person">
    <p class="person__name">Lachie Westergaard</p>
    <p class="person__role">Director</p>
  </div>
  <div class="divider"></div>

  <ul class="contacts">
    <li><svg viewBox="0 0 16 16"><path d="M4 0h8a1 1 0 0 1 1 1v14a1 1 0 0 1-1 1H4a1 1 0 0 1-1-1V1a1 1 0 0 1 1-1zm1 2v10h6V2zm3 11a1 1 0 1 0 0 2 1 1 0 0 0 0-2z"/></svg>027 519 2764</li>
    <li><svg viewBox="0 0 16 16"><path d="M1 5c0-2 3-3 7-3s7 1 7 3v1h-4V5H5v1H1zm3 2h8l2 7H2zm4 2a2 2 0 1 0 0 4 2 2 0 0 0 0-4z"/></svg>07 842 1937</li>
    <li><svg viewBox="0 0 16 16"><path d="M0 3h16v10H0zm1.5 1.2v.3L8 9l6.5-4.5v-.3zM1.5 6v5.8h13V6L8 10.5z"/></svg>office@ridgebackmotors.co.nz</li>
    <li><svg viewBox="0 0 16 16"><path d="M8 0a8 8 0 1 0 0 16A8 8 0 0 0 8 0zm0 1.5c1 0 2 2 2.3 5.5H5.7C6 3.5 7 1.5 8 1.5zM1.6 7h2.6c.1-2 .5-3.7 1.2-4.8A6.5 6.5 0 0 0 1.6 7zm10.2 0h2.6a6.5 6.5 0 0 0-3.8-4.8c.7 1.1 1.1 2.8 1.2 4.8zM1.6 9a6.5 6.5 0 0 0 3.8 4.8C4.7 12.7 4.3 11 4.2 9zm4.1 0c.3 3.5 1.3 5.5 2.3 5.5s2-2 2.3-5.5zm6.1 0c-.1 2-.5 3.7-1.2 4.8A6.5 6.5 0 0 0 14.4 9z"/></svg>ridgebackmotors.co.nz</li>
  </ul>

  <p class="address">
    <svg viewBox="0 0 14 18"><path d="M7 0a7 7 0 0 0-7 7c0 5 7 11 7 11s7-6 7-11a7 7 0 0 0-7-7zm0 4a3 3 0 1 1 0 6 3 3 0 0 1 0-6z"/></svg>
    48 Marlow Lane Whitianga 3510
  </p>

  <svg class="stripe" viewBox="0 0 680 14" preserveAspectRatio="none" aria-hidden="true">
    <rect x="0" y="0" width="680" height="14" fill="var(--ink)"/>
    <polygon points="0,0 290,0 280,14 0,14" fill="var(--red)"/>
  </svg>
</section>

</body>
</html>
```